1 pg ad for national oil & gas publication

We need a fresh version of a draft ad we have for insertion in a national publication for oil and gas land service firms. The readers of the publication are other service firms and individuals and our clients - the in-house "landmen" at the oil and gas companies. Attached is what we drafted. We want something better, but definitely including our logo.

```html
<!DOCTYPE html>
<html lang="en">
<head>
<meta charset="utf-8">
<title>Ridgeline Land Services — Full Page Ad</title>
<link rel="stylesheet" href="https://fonts.googleapis.com/css2?family=Carlito:ital,wght@0,400;0,700;1,400;1,700&family=Tinos:ital,wght@1,400;1,700&display=swap">
<style>
  :root {
    --ink: #111111;
    --paper: #ffffff;
    --frame: #1a1a1a;
    --accent-orange: #e07a1c;
    --oil-dark: #7a2e08;
    --oil-mid: #b8520f;
    --oil-light: #e39a3c;
  }
  html, body {
    margin: 0;
    padding: 0;
    width: 900px;
    height: 1200px;
    overflow: hidden;
    background: var(--paper);
  }
  .ad {
    position: relative;
    width: 900px;
    height: 1200px;
    overflow: hidden;
    background: var(--paper);
    font-family: "Carlito", "Calibri", sans-serif;
    color: var(--ink);
  }
  .ad-frame {
    position: absolute;
    inset: 14px;
    border: 3px solid var(--frame);
    border-radius: 14px;
    overflow: hidden;
    background: var(--paper);
  }
  .bubble-field {
    position: absolute;
    right: 0;
    top: 0;
    width: 380px;
    height: 960px;
    background: linear-gradient(180deg,
      rgba(90,169,230,0.55) 0%,
      rgba(127,211,208,0.45) 25%,
      rgba(169,216,106,0.45) 50%,
      rgba(232,226,122,0.40) 65%,
      rgba(245,192,138,0.45) 85%,
      rgba(245,192,138,0.0) 100%);
    -webkit-mask-image: linear-gradient(90deg, transparent 0%, #000 60%);
            mask-image: linear-gradient(90deg, transparent 0%, #000 60%);
  }
  .oil-splash {
    position: absolute;
    left: 0;
    top: 0;
    width: 866px;
    height: 1166px;
  }
  .brand-name {
    position: absolute;
    left: 0;
    right: 0;
    top: 18px;
    margin: 0;
    text-align: center;
    font-weight: 400;
    color: var(--ink);
    line-height: 0.92;
  }
  .brand-name .line-one { display: block; font-size: 138px; }
  .brand-name .line-two { display: block; font-size: 104px; }
  .tagline {
    position: absolute;
    left: 32px;
    top: 305px;
    margin: 0;
    font-style: italic;
    font-size: 28px;
    line-height: 36px;
    white-space: nowrap;
  }
  .intro, .services-list, .positioning {
    position: absolute;
    left: 13px;
    margin: 0;
    font-style: italic;
    font-size: 18px;
    line-height: 24px;
    white-space: nowrap;
  }
  .intro { top: 361px; }
  .intro strong { font-weight: 700; }
  .offer-heading {
    position: absolute;
    left: 0;
    top: 467px;
    margin: 0;
    font-style: italic;
    font-weight: 400;
    font-size: 22px;
    line-height: 32px;
    white-space: nowrap;
  }
  .offer-heading .offer-line { display: block; }
  .offer-heading .offer-line-one { margin-left: 299px; font-style: normal; }
  .offer-heading .offer-line-two { margin-left: 103px; }
  .offer-heading .highlight { color: var(--accent-orange); font-style: normal; }
  .services-list { top: 544px; font-size: 17px; }
  .positioning { top: 675px; }
  .contact {
    position: absolute;
    margin: 0;
    text-align: center;
    font-family: "Tinos", "Times New Roman", serif;
    font-style: italic;
    font-size: 13.5px;
    line-height: 21.5px;
    white-space: nowrap;
  }
  .contact .contact-title { font-weight: 700; text-transform: uppercase; }
  .contact .contact-phone { font-weight: 700; }
  .contact .contact-email { font-style: normal; font-size: 14.5px; }
  .contact-vp { left: 205px; top: 787px; width: 360px; }
  .contact-president { left: 323px; top: 865px; width: 360px; }
</style>
</head>
<body>
<main class="ad">
  <div class="ad-frame">
    <div class="bubble-field" role="img" aria-label="Soft field of translucent bubbles shading from blue through green and yellow to peach"></div>

    <svg class="oil-splash" viewBox="0 0 866 1166" role="img" aria-label="Flowing splash of amber crude oil sweeping across the lower page">
      <defs>
        <linearGradient id="oilFlow" x1="0" y1="0" x2="1" y2="1">
          <stop offset="0" stop-color="#e39a3c"/>
          <stop offset="0.45" stop-color="#b8520f"/>
          <stop offset="1" stop-color="#7a2e08"/>
        </linearGradient>
      </defs>
      <path d="M0 773 C100 790 200 880 383 943 C500 975 650 965 866 960 L866 1125 C650 1080 400 1060 0 1043 Z" fill="url(#oilFlow)" opacity="0.92"/>
    </svg>

    <h1 class="brand-name">
      <span class="line-one">Ridgeline</span>
      <span class="line-two">Land Services</span>
    </h1>

    <p class="tagline">Expertly serving oil and gas stakeholders</p>

    <p class="intro"><strong>Ridgeline Land Services</strong> is a full-service consulting firm providing<br>professional land services to the oil and gas industry, attorneys,<br>utilities, title insurers, pipeline companies, developers, land<br>owners and public agencies.</p>

    <h2 class="offer-heading">
      <span class="offer-line offer-line-one">Ridgeline Land Services is</span>
      <span class="offer-line offer-line-two"><span class="highlight">Full Service Land Company</span> a providing:</span>
    </h2>

    <p class="services-list">Oil, Gas &amp; Mineral Consulting, Leasing ARC/GIS Mapping,<br>Surface and Mineral Acquisitions, Right-of-Way Title and Acquisitions,<br>Secure Online Maps, Permitting and Regulatory Compliance,<br>Due Diligence, Land Administration, Title Research, File Management,<br>Expert Witness, Title Curative / Probate Matters, Seismic Permitting</p>

    <p class="positioning">Our firm is uniquely positioned to assist with leasing, permitting,<br>acquisitions, divestitures, due diligence and the day-to-day operational<br>challenges of drilling and producing in high density urban environments<br>throughout the Country.</p>

    <address class="contact contact-vp">
      <span class="contact-title">Dale Whitaker, RPL Vice President</span><br>
      <span class="contact-phone">(337) 555-0142</span><br>
      <span class="contact-email">dwhitaker@ridgelineland.com</span>
    </address>

    <address class="contact contact-president">
      <span class="contact-title">M. Joan Everly, Esq. President</span><br>
      <span class="contact-phone">(310)555-0198</span><br>
      <span class="contact-email">jeverly@ridgelineland.com</span>
    </address>
  </div>
</main>
</body>
</html>
```